Label design for high quality nutritional supplement brand

We need a new label design for our dietary supplement brand "Morelle" from Germany. We sell high-quality nutritional supplements that help improve overall well-being.

All products in our range should receive the new label. You can find our current design on our homepage morelle-brightfield.com. The new design should be completely redesigned and look modern, fresh, high quality, minimalist and clean. We prefer the colors nude, green and earth tones.

The newly created label should contain our Morelle logo. For this reason you will find this file attached. You will also find our current label, which needs to be renewed, in the appendix.

Colors

Designer to choose colors to be used in the design.

Requirements
Must have
• Morelle logo

```html
<!DOCTYPE html>
<html lang="de">
<head>
<meta charset="utf-8">
<title>Daily Bloom Protein-Shake – Morelle</title>
<link href="https://fonts.googleapis.com/css2?family=Arimo:wght@400;700&family=Parisienne&display=swap" rel="stylesheet">
<style>
  :root {
    --page: #ffffff;
    --label: #ececec;
    --ink: #1f1f1f;
    --gold: #c8b48a;
    --gold-light: #dccca6;
    --gold-text: #cbb98f;
    --vanilla-dark: #5a3d2a;
    --vanilla-light: #f1efe4;
  }
  * { margin: 0; padding: 0; box-sizing: border-box; }
  html, body {
    width: 1200px; height: 1200px; overflow: hidden;
    background: var(--page);
  }
  .label {
    position: absolute;
    left: 137px; top: 61px;
    width: 974px; height: 1135px;
    transform: scale(0.95);
    transform-origin: top left;
    background: linear-gradient(90deg, #dedede 0%, var(--label) 12%, #f4f4f4 50%, var(--label) 88%, #dedede 100%);
    font-family: "Arimo", Arial, sans-serif;
    color: var(--ink);
  }
  .product-name {
    position: absolute; left: 125px; top: 64px;
    font-size: 123px; font-weight: 700; line-height: 1;
    letter-spacing: 0;
  }
  .product-type {
    position: absolute; left: 134px; top: 217px;
    font-size: 62px; font-weight: 400; line-height: 1;
  }
  .category-band {
    position: absolute; left: 120px; top: 313px;
    width: 647px; height: 72px;
    background: linear-gradient(90deg, var(--gold-light), var(--gold) 50%, var(--gold-light));
    display: flex; align-items: center;
    padding-left: 25px;
    font-size: 44px; line-height: 1;
  }
  .description {
    position: absolute; left: 122px; top: 428px;
    font-size: 38px; line-height: 52px;
  }
  .flavour {
    position: absolute; left: 608px; top: 430px;
    font-family: "Parisienne", cursive;
    font-size: 68px; line-height: 1;
    color: var(--gold-text);
  }
  .flavour-illustration {
    position: absolute; left: 527px; top: 520px;
    width: 345px; height: 155px;
    border-radius: 40px;
    background: radial-gradient(ellipse at 55% 45%, var(--vanilla-light) 0%, #e6e2d4 30%, #8a6a52 60%, var(--vanilla-dark) 80%, transparent 100%);
  }
  .brand {
    position: absolute; left: 200px; top: 810px;
    display: flex; align-items: center; gap: 28px;
  }
  .brand-mark {
    width: 44px; height: 44px; border-radius: 50%;
    background: var(--gold);
  }
  .brand-name {
    font-size: 120px; font-weight: 400; line-height: 1;
    color: var(--ink);
  }
  .bottom-band {
    position: absolute; left: 0; top: 1043px;
    width: 100%; height: 48px;
    background: linear-gradient(90deg, var(--gold-light), var(--gold) 50%, var(--gold-light));
  }
  .net-weight {
    position: absolute; left: 0; top: 1097px;
    width: 100%; text-align: center;
    font-size: 30px; line-height: 1;
  }
</style>
</head>
<body>
  <div class="label">
    <h1 class="product-name">DAILY BLOOM</h1>
    <p class="product-type">PROTEIN-SHAKE</p>
    <div class="category-band">Nahrungsergänzungsmittel</div>
    <p class="description">Whey Protein-Pulver mit<br>Flohsamenschalen</p>
    <p class="flavour">Vanille</p>
    <div class="flavour-illustration" role="img" aria-label="Vanilleblüte mit Blättern auf Vanilleschoten"></div>
    <div class="brand">
      <span class="brand-mark"></span>
      <span class="brand-name">Morelle</span>
    </div>
    <div class="bottom-band"></div>
    <p class="net-weight">630g</p>
  </div>
</body>
</html>
```